Flyer needed For the Council for Stewardship of Public Works

With an increasing need for professional staffing in our design and construction industry it is important for organizations to be able to attract, support, and retain people of all genders. With the increase of women entering the design/construction industry, we need to be able to identify and address the specific needs of women in our industry, including those A/E’s who are on the facility Owner side.

This Forum will provide a venue to openly discuss the issues affecting our industry and ideas to address those issues.The program includes time for presentations and a panel discussion by accomplished women in our industry, and facilitated table and open discussions to form solutions with your peers. You will come away with ideas you can implement within your organization to build processes and a supportive culture for women

IN THE ATTACHMENTS
* you'll find our company logo

Target Market(s)

Women in the design and construction industry

Industry/Entity Type

Construction

Requirements
Must have
• Logo, event name, date, time, location, panelists names and pics, NBF continuing education provided, contact information: Maren Holtzclaw, maren.holtzclaw@c-sfpw.org, (555) 740-1938
• Register at: www.c-sfpw.org/events
• Design should encompass the description given above.
Nice to have
• Colors that compliment our logo

```html
<!DOCTYPE html>
<html lang="en">
<head>
<meta charset="utf-8">
<title>AEC Industry Women's Mini Forum &amp; Workshop</title>
<link href="https://fonts.googleapis.com/css2?family=Oswald:wght@400;500;700&family=Open+Sans:ital,wght@0,400;0,600;1,600&display=swap" rel="stylesheet">
<style>
  :root {
    --sky: #8ad2e6;
    --navy: #1d2a5c;
    --green: #8cc63f;
    --green-dark: #5d9b2a;
    --blue: #1a78bd;
    --white: #ffffff;
    --badge: #111111;
    --portrait: #5f8fa6;
  }
  * { margin: 0; padding: 0; box-sizing: border-box; }
  html, body { width: 857px; height: 1200px; overflow: hidden; }
  body { background: var(--sky); font-family: "Open Sans", sans-serif; color: var(--navy); }
  .flyer { position: relative; width: 857px; height: 1200px; overflow: hidden; background: var(--sky); }

  .brand { position: absolute; left: 24px; top: 20px; display: flex; align-items: center; gap: 14px; }
  .brand-mark { width: 56px; height: 56px; background: var(--green); }
  .brand-name { font-family: "Oswald", sans-serif; font-weight: 700; font-size: 46px; color: var(--white); line-height: 1; }
  .brand-sub { position: absolute; left: 24px; top: 84px; font-family: "Oswald", sans-serif; font-weight: 500; font-size: 13px; color: var(--white); letter-spacing: .3px; }

  .ce-badge { position: absolute; right: 18px; top: 14px; width: 112px; height: 112px; border-radius: 50%; background: var(--badge); }

  .headline { position: absolute; top: 168px; left: 0; width: 100%; text-align: center; }
  .event-industry { font-family: "Oswald", sans-serif; font-weight: 700; font-size: 46px; color: var(--navy); line-height: 1.05; }
  .event-name { font-family: "Oswald", sans-serif; font-weight: 500; font-size: 40px; color: var(--green); line-height: 1.15; }
  .event-date { font-family: "Oswald", sans-serif; font-weight: 700; font-size: 38px; color: var(--navy); line-height: 1.1; }
  .event-time { font-family: "Oswald", sans-serif; font-weight: 500; font-size: 22px; color: var(--navy); line-height: 1.3; }
  .event-venue { font-style: italic; font-weight: 600; font-size: 19px; color: var(--white); line-height: 1.35; }

  .program { position: absolute; top: 388px; left: 60px; width: 737px; text-align: center; font-size: 17px; line-height: 22.5px; color: var(--navy); }

  .panelists { position: absolute; top: 754px; left: 40px; width: 777px; display: flex; justify-content: space-between; list-style: none; }
  .panelist { width: 150px; display: flex; flex-direction: column; align-items: center; text-align: center; }
  .panelist-photo { width: 44px; height: 44px; border-radius: 50%; background: var(--portrait); border: 2px solid var(--white); }
  .panelist-name { font-weight: 600; font-size: 12.5px; line-height: 15px; margin-top: 3px; color: var(--navy); }
  .panelist-role { font-size: 11.5px; line-height: 13px; color: var(--navy); }

  .credit { position: absolute; top: 836px; left: 0; width: 100%; text-align: center; font-family: "Open Sans", sans-serif; font-weight: 400; font-size: 40px; line-height: 52px; color: var(--blue); }

  .contact-band { position: absolute; left: 0; top: 895px; width: 857px; height: 225px; }
  .contact { position: absolute; top: 935px; left: 0; width: 100%; text-align: center; color: var(--navy); }
  .contact-name { font-family: "Oswald", sans-serif; font-weight: 500; font-size: 28px; line-height: 40px; color: var(--navy); }
  .contact-line { font-size: 20px; line-height: 34px; }

  .register { position: absolute; left: 0; top: 1118px; width: 857px; height: 82px; background: var(--white); display: flex; align-items: center; justify-content: center; font-family: "Oswald", sans-serif; font-weight: 400; font-size: 30px; color: var(--navy); }
</style>
</head>
<body>
<main class="flyer">
  <div class="brand">
    <span class="brand-mark"></span>
    <span class="brand-name">C-SfPW</span>
  </div>
  <div class="brand-sub">Council for Stewardship of Public Works</div>

  <div class="ce-badge" aria-hidden="true"></div>

  <header class="headline">
    <h1 class="event-industry">AEC INDUSTRY</h1>
    <h2 class="event-name">Women's Mini Forum &amp; Workshop</h2>
    <p class="event-date">JANUARY 13 2016</p>
    <p class="event-time">8:30 AM – 12:30 PM</p>
    <p class="event-venue">Larkspur Suites, San Marcos, Texas</p>
  </header>

  <p class="program">
    The program includes time for presentations<br>
    and a panel discussion by<br>
    accomplished women in our industry,<br>
    and facilitated table and open discussions to form<br>
    solutions with your peers.<br>
    You will come away with ideas you can implement<br>
    within your organization<br>
    to build processes and a supportive culture for women.<br>
    A visual note-taker and separate scribe<br>
    will be utilized to compile ideas and solutions,<br>
    for distribution to participants after the event.<br>
    Presenters and Panelists: architect, engineer,<br>
    contractor, sub/trade, facility Owner<br>
    Table Facilitators: one for each table,<br>
    with tables divided into industry segments:<br>
    architects, engineers, contractors, subs/trades, Owners.
  </p>

  <ul class="panelists">
    <li class="panelist">
      <span class="panelist-photo" role="img" aria-label="Portrait photo of panelist Dana Whitcombe"></span>
      <span class="panelist-name">Dana Whitcombe</span>
      <span class="panelist-role">Architect</span>
    </li>
    <li class="panelist">
      <span class="panelist-photo" role="img" aria-label="Portrait photo of panelist Priya Okafor"></span>
      <span class="panelist-name">Priya Okafor</span>
      <span class="panelist-role">Engineer</span>
    </li>
    <li class="panelist">
      <span class="panelist-photo" role="img" aria-label="Portrait photo of panelist Lena Marsh"></span>
      <span class="panelist-name">Lena Marsh</span>
      <span class="panelist-role">Contractor</span>
    </li>
    <li class="panelist">
      <span class="panelist-photo" role="img" aria-label="Portrait photo of panelist Rosa Delvane"></span>
      <span class="panelist-name">Rosa Delvane</span>
      <span class="panelist-role">Sub/Trade</span>
    </li>
    <li class="panelist">
      <span class="panelist-photo" role="img" aria-label="Portrait photo of panelist Joan Kettering"></span>
      <span class="panelist-name">Joan Kettering</span>
      <span class="panelist-role">Facility Owner</span>
    </li>
  </ul>

  <p class="credit">NBF continuing education</p>

  <svg class="contact-band" viewBox="0 0 857 225" aria-hidden="true">
    <defs>
      <linearGradient id="swoosh" x1="0" y1="0" x2="1" y2="0">
        <stop offset="0" stop-color="#5d9b2a"/>
        <stop offset=".5" stop-color="#8cc63f"/>
        <stop offset="1" stop-color="#5d9b2a"/>
      </linearGradient>
    </defs>
    <path d="M0 70 Q428 -20 857 70 L857 225 L0 225 Z" fill="url(#swoosh)"/>
    <ellipse cx="428" cy="120" rx="330" ry="95" fill="#ffffff"/>
  </svg>

  <section class="contact">
    <p class="contact-name">Contact : Maren Holtzclaw</p>
    <p class="contact-line">maren.holtzclaw@c-sfpw.org</p>
    <p class="contact-line">(555) 740-1938</p>
  </section>

  <footer class="register">Register at: www.c-sfpw.org/events</footer>
</main>
</body>
</html>
```